Bloom Where You Stand redesign book cover

A new cover for my already published book. The old cover looks great but not for a women’s self help book. Cover is killing sales. Once I explain the book it sells quickly AND gets 5 star reviews. Outside of actually explaining the book the cover scares people away. I need a new cover. ASAP! Before The yr end please.
The tag line -
Discover 10 Practical Ways To Replace negative thoughts with knowing the voice of God. This is a self help book for women 35-45 Christian but not religious. Each chapter is a hands on spiritual experience where the reader takes small tests about themselves, discover why they have negative thoughts, what they are and how to listen to God through hands on methods of listening. NOT strange type of things. They learn what 4 voices they are listening to and how to hone in on Jesus voice. There are scriptures to pray and journaling assignments. The old cover is in the brief with the write up for the back of the book. Please use the new author picture, Publishers logo (tree), barcode, and contact info from the back of the book. And yes the author name and title of the book on the spine. Lay out on the back cover needs to be interesting. You have all the info have fun with it.

Target Market(s)

Women 35-45 yrs old Christian and new believers or seekers.

Industry/Entity Type

Non profit organization. Missionary

Requirements
Must have
• Something DIFFERENT than what is there now. Something inviting. Fresh clear title
Nice to have
• Multi colors however a white stand out cover is also good.
Should not have
• Heavy religious feeling. No church steeples, Jesus faces.

```html
<!DOCTYPE html>
<html lang="en">
<head>
<meta charset="utf-8">
<title>Bloom Where You Stand — Book Cover</title>
<link rel="stylesheet" href="https://fonts.googleapis.com/css2?family=Bebas+Neue&family=Montserrat:wght@700;800&family=Poppins:wght@600&display=swap">
<style>
  :root {
    --sky-deep: #0f5a5c;
    --sky-mid: #2b7a76;
    --sky-light: #4f9490;
    --sun-yellow: #f9c93a;
    --ink-white: #ffffff;
    --ghost: rgba(255, 255, 255, 0.2);
    --rooftop-dark: #1d2826;
    --rooftop-mid: #2c3a37;
  }
  * { margin: 0; padding: 0; box-sizing: border-box; }
  html, body { width: 848px; height: 1200px; overflow: hidden; background: var(--sky-deep); }
  .cover {
    position: relative;
    width: 848px;
    height: 1200px;
    overflow: hidden;
  }
  .sky-backdrop {
    position: absolute; inset: 0;
    background:
      radial-gradient(ellipse 340px 160px at 640px 140px, rgba(120,170,160,0.35), transparent 70%),
      radial-gradient(ellipse 300px 140px at 120px 260px, rgba(120,170,160,0.3), transparent 70%),
      radial-gradient(ellipse 400px 160px at 300px 1080px, rgba(120,170,160,0.25), transparent 70%),
      linear-gradient(180deg, var(--sky-mid) 0%, var(--sky-deep) 45%, var(--sky-mid) 75%, var(--sky-light) 100%);
  }
  .ghost-letters {
    position: absolute;
    font-family: 'Poppins', sans-serif;
    font-weight: 600;
    color: var(--ghost);
    line-height: 1;
    letter-spacing: -10px;
    white-space: nowrap;
  }
  .ghost-letters--top { top: 20px; left: 72px; font-size: 560px; }
  .ghost-letters--bottom { top: 640px; left: -80px; font-size: 560px; }
  .brush-band { position: absolute; left: 0; top: 340px; width: 848px; height: 400px; }
  .rooftop-photo {
    position: absolute;
    left: 476px; top: 1010px;
    width: 372px; height: 190px;
    background: linear-gradient(180deg, var(--rooftop-mid) 0%, var(--rooftop-dark) 100%);
  }
  .title {
    position: absolute;
    inset: 0;
    font-family: 'Bebas Neue', sans-serif;
    font-weight: 400;
    color: var(--ink-white);
    text-shadow: 0 6px 14px rgba(0,0,0,0.35);
  }
  .title__line {
    position: absolute;
    left: 0; width: 848px;
    text-align: center;
    line-height: 0.86;
    white-space: nowrap;
  }
  .title__line--first { top: 221px; font-size: 232px; }
  .title__line--middle { top: 470px; font-size: 150px; }
  .title__line--last { top: 659px; font-size: 232px; }
  .tagline {
    position: absolute;
    left: 0; width: 848px; top: 894px;
    text-align: center;
    font-family: 'Montserrat', sans-serif;
    font-weight: 700;
    font-size: 19px;
    line-height: 1.35;
    color: var(--ink-white);
    margin-left: -20px;
  }
  .author {
    position: absolute;
    left: 0; width: 848px; top: 1024px;
    text-align: center;
    font-family: 'Montserrat', sans-serif;
    font-weight: 800;
    font-size: 31px;
    color: var(--ink-white);
    margin-left: 20px;
  }
</style>
</head>
<body>
  <main class="cover">
    <div class="sky-backdrop" role="img" aria-label="Photograph of a cloudy teal sky"></div>

    <div class="ghost-letters ghost-letters--top" aria-hidden="true">ST</div>
    <div class="ghost-letters ghost-letters--bottom" aria-hidden="true">AND</div>

    <svg class="brush-band" viewBox="0 0 848 400" aria-hidden="true">
      <path fill="var(--sun-yellow)" d="M0 80 L40 70 L90 82 L140 60 L200 72 L260 50 L330 62 L400 40 L470 48 L540 30 L610 22 L680 14 L740 20 L800 28 L848 40
        L848 270 L820 262 L790 280 L750 266 L700 284 L650 272 L600 292 L540 280 L480 300 L420 288 L360 310 L300 296 L240 318 L180 302 L120 322 L70 306 L30 324 L0 312 Z"/>
      <g fill="var(--sun-yellow)" opacity="0.85">
        <circle cx="60" cy="62" r="5"/><circle cx="150" cy="48" r="4"/><circle cx="230" cy="58" r="6"/>
        <circle cx="380" cy="30" r="4"/><circle cx="560" cy="18" r="5"/><circle cx="720" cy="8" r="4"/>
        <circle cx="90" cy="334" r="5"/><circle cx="210" cy="326" r="4"/><circle cx="330" cy="320" r="6"/>
        <circle cx="460" cy="312" r="4"/><circle cx="620" cy="302" r="5"/><circle cx="770" cy="292" r="4"/>
      </g>
    </svg>

    <div class="rooftop-photo" role="img" aria-label="Photograph of a dark rooftop against the sky"></div>

    <h1 class="title">
      <span class="title__line title__line--first">BLOOM</span>
      <span class="title__line title__line--middle">WHERE YOU</span>
      <span class="title__line title__line--last">STAND</span>
    </h1>

    <p class="tagline">Discover 10 Practical Ways To Replace<br>negative thoughts with knowing the voice of God.</p>

    <p class="author">Lena Marsh</p>
  </main>
</body>
</html>
```